Faithful Oaks Fellowship (FOF)
• The Prayer arm of GRCA which enables members to delight themselves in the purpose and work of God
• Equip members with the instrument of prayer to walk with God so that they can make lasting changes here on Earth
• Coordinate projects like the Dawn Vigil Circle, Lantern Night Vigil Series, Chain Prayers, Prayer Projects, Prayer Retreats, and the Worldwide Vigil Circle
• Manage the GRCA Prayer Academy
• Goal is transformation and dominion
• Build members to stand as mighty men giving themselves continually to prayer

You learn how to pray by praying
Join the Faithful Oaks Fellowship!

```html
<!DOCTYPE html>
<html lang="en">
<head>
<meta charset="utf-8">
<title>Faithful Oaks Fellowship</title>
<link rel="stylesheet" href="https://fonts.googleapis.com/css2?family=Bebas+Neue&family=Arimo:wght@400;700&display=swap">
<style>
  :root {
    --sky-deep: #0a2f9c;
    --sky-mid: #1c5fe0;
    --sky-light: #7fb4f5;
    --cloud: #e9f1fb;
    --text-white: #ffffff;
    --chrome-top: #ffffff;
    --chrome-mid: #d4d8de;
    --chrome-low: #8b929c;
    --stripe-white: #f7f7f5;
    --stripe-grey: #a9a9a9;
    --gold-light: #fbf6ea;
    --gold-mid: #e9d9b4;
    --gold-deep: #c9ab6f;
    --brand-ink: #1f5a56;
  }
  * { margin: 0; padding: 0; box-sizing: border-box; }
  html, body { width: 848px; height: 1200px; overflow: hidden; background: #fff; }
  .poster {
    position: relative;
    width: 848px;
    height: 1200px;
    overflow: hidden;
    font-family: "Arimo", Arial, sans-serif;
  }
  .sky {
    position: absolute;
    left: 0; top: 0;
    width: 848px; height: 896px;
    background:
      radial-gradient(ellipse 520px 260px at 50% 330px, rgba(190,220,255,0.55), rgba(190,220,255,0) 70%),
      radial-gradient(ellipse 260px 120px at 8% 150px, var(--cloud), rgba(233,241,251,0) 75%),
      radial-gradient(ellipse 300px 110px at 92% 90px, var(--cloud), rgba(233,241,251,0) 75%),
      radial-gradient(ellipse 420px 120px at 50% 20px, rgba(233,241,251,0.85), rgba(233,241,251,0) 75%),
      linear-gradient(180deg, var(--sky-light) 0%, var(--sky-mid) 30%, var(--sky-deep) 100%);
  }
  .brand {
    position: absolute;
    top: 48px; left: 0; width: 848px;
    display: flex; align-items: center; justify-content: center; gap: 16px;
  }
  .brand-mark {
    width: 96px; height: 96px; border-radius: 50%;
    background: #ffffff;
    border: 4px solid var(--brand-ink);
  }
  .brand-name {
    font-size: 24px; font-weight: 700; color: var(--brand-ink);
    line-height: 1.15; width: 240px;
  }
  .title, .acronym, .cta {
    position: absolute; left: 0; width: 848px; text-align: center;
    font-family: "Bebas Neue", Impact, sans-serif;
  }
  .title, .acronym {
    background: linear-gradient(180deg, var(--chrome-top) 0%, var(--chrome-mid) 55%, var(--chrome-low) 62%, var(--chrome-top) 100%);
    -webkit-background-clip: text; background-clip: text; color: transparent;
    filter: drop-shadow(0 3px 2px rgba(0,0,30,0.6));
  }
  .title { top: 190px; font-size: 100px; line-height: 1; letter-spacing: -1px; }
  .acronym { top: 300px; font-size: 54px; line-height: 1; }
  .duties {
    position: absolute; top: 410px; left: 96px; width: 680px;
    list-style: none; color: var(--text-white);
    font-size: 23px; line-height: 1.2;
  }
  .duties li { margin-bottom: 20px; }
  .duties li::before { content: "•"; margin-right: 4px; }
  .stripe {
    position: absolute; left: 0; top: 896px; width: 848px; height: 24px;
    background: var(--stripe-white);
    border-top: 3px solid var(--stripe-grey);
    border-bottom: 2px solid #d8d3c6;
  }
  .footer {
    position: absolute; left: 0; top: 920px; width: 848px; height: 280px;
    background: linear-gradient(180deg, var(--gold-light) 0%, var(--gold-mid) 45%, var(--gold-deep) 100%);
  }
  .cta {
    color: var(--text-white);
    font-size: 64px; line-height: 1;
    text-shadow: 0 3px 4px rgba(0,0,0,0.55), 0 0 2px rgba(0,0,0,0.4);
  }
  .cta-learn { top: 972px; }
  .cta-join { top: 1046px; font-size: 60px; }
</style>
</head>
<body>
  <main class="poster">
    <div class="sky" role="img" aria-label="Bright blue sky with white clouds and rays of light"></div>

    <header class="brand">
      <span class="brand-mark"></span>
      <span class="brand-name">Grace Rock Christian Assembly</span>
    </header>

    <h1 class="title">Faithful Oaks Fellowship</h1>
    <p class="acronym">(FOF)</p>

    <ul class="duties">
      <li>The <b>Prayer arm</b> of GRCA which enables members to delight themselves in the purpose and work of God</li>
      <li><b>Equip</b> members with the instrument of prayer to walk with God so that they can make lasting changes here on Earth</li>
      <li><b>Coordinate</b> projects like the Dawn Vigil Circle, Lantern Night Vigil Series, Chain Prayers, Prayer Projects, Prayer Retreats, and the Worldwide Vigil Circle</li>
      <li><b>Manage</b> the GRCA Prayer Academy</li>
      <li><b>Goal</b> is transformation and dominion</li>
      <li><b>Build</b> members to stand as mighty men giving themselves continually to prayer</li>
    </ul>

    <div class="stripe"></div>
    <div class="footer"></div>
    <p class="cta cta-learn">You learn how to pray by praying</p>
    <p class="cta cta-join">Join the Faithful Oaks Fellowship!</p>
  </main>
</body>
</html>
```